Marlow Crest Holdings (Remodeling company) needs a logo and business card

We need a business card design for a new company. We "flip" upmarket houses (buy, remodel and sell) in the Austin, TX area. I'd like neutral colors (grey, white, gold black). I would like it to include a simple, clean logo. Our designs are modern and uncluttered and I would like that reflected in the business card design.

Target Market(s)

Young professionals, Families, Retirees. Our properties will sell for $750k+

Industry/Entity Type

Real Estate

Contact Information for Business Card

Marlow Crest Holdings
Nora Pellham
(555) 216 7042
Owner
Rory Tansil
(555) 638 1975
Realtor

Logo Text

Marlow Crest Holdings

Font styles to use
Serif
Script

Requirements
Must have
• Simple, classic design
Nice to have
• Clean lines, modern look
Should not have
• Too traditionally

```html
<!DOCTYPE html>
<html lang="en">
<head>
<meta charset="utf-8">
<title>Marlow Crest Holdings – Business Card</title>
<link rel="stylesheet" href="https://fonts.googleapis.com/css2?family=Lexend:wght@400;500&family=Open+Sans:wght@400&display=swap">
<style>
  :root {
    --canvas: #a9a5a6;
    --card: #f7f6f5;
    --ink: #1c1c1c;
    --muted: #5a5a5a;
    --gold: #c99a3a;
    --black: #141414;
    --room-light: #fbfaf9;
    --room-shade: #e9e6e3;
  }
  * { box-sizing: border-box; margin: 0; padding: 0; }
  html, body { width: 1200px; height: 1200px; overflow: hidden; }
  body { background: var(--canvas); position: relative; font-family: "Open Sans", sans-serif; }

  .card {
    position: absolute;
    width: 712px;
    height: 418px;
    border-radius: 24px;
    background: var(--card);
    overflow: hidden;
  }
  .card--front { left: 238px; top: 119px; }
  .card--back  { left: 230px; top: 644px; }

  .card__backdrop {
    position: absolute; inset: 0;
    background: linear-gradient(135deg, var(--room-light) 0%, var(--room-shade) 55%, var(--room-light) 100%);
    opacity: .8;
  }

  .brand-name {
    position: absolute;
    font-family: "Lexend", sans-serif;
    font-weight: 400;
    color: var(--ink);
    white-space: nowrap;
    letter-spacing: .5px;
  }
  .card--front .brand-name { left: 0; right: 0; top: 204px; text-align: center; font-size: 40px; }
  .card--back .brand-name { left: 48px; top: 106px; font-size: 29px; }

  .holder { position: absolute; left: 48px; top: 250px; }
  .holder__name { font-family: "Lexend", sans-serif; font-weight: 400; font-size: 25px; color: var(--ink); letter-spacing: .5px; }
  .holder__role { font-size: 15px; color: var(--muted); margin-top: 8px; }

  .contact { position: absolute; left: 306px; top: 250px; list-style: none; }
  .contact__item { display: flex; align-items: center; height: 26.5px; font-size: 17px; color: var(--ink); }
  .contact__icon { width: 16px; height: 16px; margin-right: 18px; flex: none; }

  .card__band { position: absolute; left: 0; bottom: 0; width: 712px; height: 22px; }
</style>
</head>
<body>

<section class="card card--front" aria-label="Card front">
  <div class="card__backdrop" role="img" aria-label="Faint photo of a bright modern living room"></div>
  <div class="brand-name">Marlow Crest Holdings</div>
</section>

<section class="card card--back" aria-label="Card back">
  <div class="card__backdrop" role="img" aria-label="Faint photo of a bright modern living room"></div>
  <div class="brand-name">Marlow Crest Holdings</div>

  <div class="holder">
    <div class="holder__name">Nora Pellham</div>
    <div class="holder__role">Owner</div>
  </div>

  <ul class="contact">
    <li class="contact__item">
      <svg class="contact__icon" viewBox="0 0 16 16" aria-hidden="true"><path fill="var(--gold)" d="M1 5c0-2 3-3 7-3s7 1 7 3v1h-3V5H4v1H1zM4 7h8l2 7H2z"/><circle cx="8" cy="10.5" r="1.8" fill="var(--card)"/></svg>
      (555) 216 7042
    </li>
    <li class="contact__item">
      <svg class="contact__icon" viewBox="0 0 16 16" aria-hidden="true"><rect x="1" y="3" width="14" height="10" fill="var(--gold)"/><path d="M1 3l7 6 7-6" fill="none" stroke="var(--card)" stroke-width="1.3"/></svg>
      nora@marlowcrestholdings.com
    </li>
    <li class="contact__item">
      <svg class="contact__icon" viewBox="0 0 16 16" aria-hidden="true"><circle cx="8" cy="8" r="7" fill="var(--gold)"/><g fill="none" stroke="var(--card)" stroke-width=".9"><ellipse cx="8" cy="8" rx="3" ry="7"/><path d="M1 8h14M2 4.5h12M2 11.5h12"/></g></svg>
      marlowcrestholdings.com
    </li>
  </ul>

  <svg class="card__band" viewBox="0 0 712 22" preserveAspectRatio="none" aria-hidden="true">
    <polygon points="0,4 500,4 480,22 0,22" fill="var(--gold)"/>
    <polygon points="503,4 712,4 712,22 483,22" fill="var(--black)"/>
  </svg>
</section>

</body>
</html>
```